Poster displaybox & poster box sticker

We need a graphic design for a displaybox for posters in suvenir shop.

On picture #1 (on left) you can see existing displaybox, which has a design we are not happy with. On pictures #2, #3, #4, #5 you can see poster designs that we are trying to sell (some or all of those posters should be on that displaybox. We feel that poster design on picture #2 is most attractive for our customers, and it should be displayed in front side of the box but we are open for suggestions). We can provide pictures with better and higher resolution if needed.

On Picture #1 (on right) you can see box which contains poster. We need graphic design for a sticker for that box. The sticker should represent the poster design which is in the box (pictures #2,#3,#4,#5). The sticker design should be compatible with the displaybox design.

Industry/Entity Type

Graphic Design

Requirements
Must have
• measures for displaybox are 28cmX16cmX28cm (lengh, width, depth), see picture #1

displaybox should display text "KESTRAVEL ART POSTER" because it is the name of our product (posters that we are trying to sell)

measures of the box for posters are 4,5cmx4,5cmx49cm and it is already made. We need a sticker that should go on that box which represents the poster design containing. Essentialy it is going to be 4 differerent stickers (for each post poster design containing) but with the same design. We feel it should be a sticker that goes around the box but we are open for any suggestions.
Nice to have
• we feel some of the design of box and sticker shoud have red color, but we are open for suggestions

```html
<!DOCTYPE html>
<html lang="en">
<head>
<meta charset="utf-8">
<title>Kestravel Art Poster – Display Box &amp; Sticker Set</title>
<link href="https://fonts.googleapis.com/css2?family=Josefin+Sans:wght@300;400&display=swap" rel="stylesheet">
<style>
  :root {
    --brand-red: #cc2447;
    --brand-red-deep: #b81e3c;
    --sunset-orange: #e8643a;
    --sunset-gold: #f2a03a;
    --harbour-blue: #2f5f9e;
    --harbour-deep: #1d3563;
    --stone-pink: #e7a58f;
    --leaf-green: #3f8a4a;
    --paper: #ffffff;
    --ink-light: #ffffff;
  }
  * { box-sizing: border-box; margin: 0; padding: 0; }
  html, body {
    width: 1200px; height: 897px; overflow: hidden;
    background: var(--paper);
    font-family: "Josefin Sans", sans-serif;
  }
  .canvas { position: relative; width: 1200px; height: 897px; overflow: hidden; }

  /* Display box front */
  .box-front {
    position: absolute; left: 0; top: 0; width: 913px; height: 897px;
    background: var(--brand-red);
    overflow: hidden;
  }
  .box-front__painting {
    position: absolute; left: 0; top: 120px; width: 913px; height: 777px;
    background:
      radial-gradient(ellipse at 25% 55%, var(--stone-pink) 0%, transparent 35%),
      radial-gradient(ellipse at 70% 30%, var(--sunset-gold) 0%, transparent 40%),
      radial-gradient(ellipse at 55% 80%, var(--harbour-blue) 0%, transparent 45%),
      radial-gradient(ellipse at 10% 92%, var(--leaf-green) 0%, transparent 25%),
      linear-gradient(180deg, var(--brand-red) 0%, var(--sunset-orange) 22%, var(--sunset-gold) 45%, var(--harbour-blue) 72%, var(--harbour-deep) 100%);
  }
  .box-front__title {
    position: absolute; left: 46px; top: 62px;
    color: var(--ink-light); font-weight: 300; line-height: 1;
  }
  .box-front__title-main {
    display: block; font-size: 66px; letter-spacing: 3px;
  }
  .box-front__title-sub {
    display: block; font-size: 50px; letter-spacing: 2px;
    text-align: right; margin-top: 8px;
  }
  .box-front__artist {
    position: absolute; left: 632px; top: 112px;
    color: var(--ink-light); font-weight: 400; font-size: 54px; line-height: 1;
  }

  /* Poster tube stickers */
  .sticker {
    position: absolute; left: 939px; width: 258px; height: 127px;
    display: flex;
  }
  .sticker__painting { width: 129px; height: 100%; }
  .sticker__label {
    width: 129px; height: 100%; background: var(--brand-red);
    position: relative; color: var(--ink-light); text-align: center;
  }
  .sticker__artist {
    position: absolute; left: 0; right: 0; top: 38px;
    font-size: 22px; font-weight: 400; line-height: 1;
  }
  .sticker__place {
    position: absolute; left: 0; right: 0; bottom: 16px;
    font-size: 13px; font-weight: 300; letter-spacing: 0.5px; line-height: 1;
  }
  .sticker--fortress { top: 20px; }
  .sticker--church { top: 164px; }
  .sticker--harbour { top: 305px; }
  .sticker--rooftops { top: 448px; }

  .sticker--fortress .sticker__painting {
    background: linear-gradient(160deg, var(--sunset-gold) 0%, #6a7fae 45%, var(--leaf-green) 75%, var(--stone-pink) 100%);
  }
  .sticker--church .sticker__painting {
    background: linear-gradient(180deg, #7fb6c8 0%, var(--sunset-gold) 45%, #8a5a2e 80%, #2b2b2b 100%);
  }
  .sticker--harbour .sticker__painting {
    background: linear-gradient(180deg, var(--sunset-gold) 0%, var(--stone-pink) 40%, var(--harbour-blue) 75%, var(--sunset-orange) 100%);
  }
  .sticker--rooftops .sticker__painting {
    background: linear-gradient(170deg, #8fc4d8 0%, var(--sunset-gold) 40%, #5a86b0 70%, var(--sunset-orange) 100%);
  }
</style>
</head>
<body>
<main class="canvas">

  <section class="box-front">
    <div class="box-front__painting" role="img" aria-label="Oil painting of a walled harbour town at sunset: fortress tower, stone walls, colourful houses and boats on reflective water"></div>
    <h1 class="box-front__title">
      <span class="box-front__title-main">KESTRAVEL</span>
      <span class="box-front__title-sub">ART POSTER</span>
    </h1>
    <p class="box-front__artist">M. Lorano</p>
  </section>

  <aside class="sticker sticker--fortress">
    <div class="sticker__painting" role="img" aria-label="Oil painting of a hilltop fortress above red-roofed houses"></div>
    <div class="sticker__label">
      <p class="sticker__artist">M. Lorano</p>
      <p class="sticker__place">DUBROVNIK</p>
    </div>
  </aside>

  <aside class="sticker sticker--church">
    <div class="sticker__painting" role="img" aria-label="Oil painting of a domed baroque church with a crowded square"></div>
    <div class="sticker__label">
      <p class="sticker__artist">M. Lorano</p>
      <p class="sticker__place">DUBROVNIK</p>
    </div>
  </aside>

  <aside class="sticker sticker--harbour">
    <div class="sticker__painting" role="img" aria-label="Oil painting of the old harbour with fortress tower and boats"></div>
    <div class="sticker__label">
      <p class="sticker__artist">M. Lorano</p>
      <p class="sticker__place">DUBROVNIK</p>
    </div>
  </aside>

  <aside class="sticker sticker--rooftops">
    <div class="sticker__painting" role="img" aria-label="Oil painting of old town rooftops and a church dome"></div>
    <div class="sticker__label">
      <p class="sticker__artist">M. Lorano</p>
      <p class="sticker__place">DUBROVNIK</p>
    </div>
  </aside>

</main>
</body>
</html>
```